Need Help having my business card stand out

I am the owner of Pine Ridge Canine Coaching and would like for my business cards to stand out. I have been trying to keep designing them myself but I can't get what I have in my head on the card. I will try my best to post templates that I like for inspirations. I want something unique but elegant. I don't want in to look cartoony or cheesy. It needs to pop in a pet shop but also in a coffee shop or gym.

Target Market(s)

Dog owners, Married ,No young kids Jr High school kids and up (maybe kids on the way) Executives, Stay at home moms/wives, Small business owners

Industry/Entity Type

Dog Training

Contact Information for Business Card

Trevor Holloway, 555-304-7162, info@pineridgecanine.example, www.pineridgecanine.example

Colors

Designer to choose colors to be used in the design.

Requirements
Must have
• my logo
Should not have
• Cursive lettering

```html
<!DOCTYPE html>
<html lang="en">
<head>
<meta charset="utf-8">
<title>Pine Ridge Canine Coaching – Business Cards</title>
<link rel="stylesheet" href="https://fonts.googleapis.com/css2?family=Open+Sans:wght@300;400;600&family=Oswald:wght@600&display=swap">
<style>
  :root {
    --backdrop: #2a2624;
    --paper: #ffffff;
    --ink: #111111;
    --band-grey: #333534;
    --name-strip: #202221;
    --text-light: #f2f2f2;
    --photo-tone-a: #5a5f66;
    --photo-tone-b: #a07a52;
    --illustration-tone: #1a1a1a;
  }
  * { box-sizing: border-box; margin: 0; padding: 0; }
  html, body { width: 1200px; height: 1200px; overflow: hidden; }
  body {
    background: var(--backdrop);
    font-family: "Open Sans", sans-serif;
    position: relative;
  }
  .card {
    position: absolute;
    left: 180px;
    width: 840px;
    height: 480px;
    background: var(--paper);
    overflow: hidden;
    box-shadow: 0 12px 30px rgba(0,0,0,0.45);
  }
  .card--front { top: 90px; }
  .card--back { top: 630px; }

  /* Front */
  .brand {
    position: absolute;
    left: 56px;
    top: 62px;
    display: flex;
    align-items: center;
    gap: 14px;
  }
  .brand__dot {
    width: 34px; height: 34px;
    border-radius: 50%;
    background: var(--ink);
  }
  .brand__name {
    font-family: "Open Sans", sans-serif;
    font-weight: 600;
    font-size: 24px;
    color: var(--ink);
    line-height: 1.2;
    width: 220px;
  }
  .contact-band {
    position: absolute;
    left: 0; right: 0;
    top: 212px;
    height: 218px;
    background: var(--band-grey);
  }
  .contact-band__name {
    height: 56px;
    background: var(--name-strip);
    color: var(--text-light);
    font-weight: 400;
    font-size: 30px;
    padding-left: 60px;
    line-height: 56px;
  }
  .contact-list {
    list-style: none;
    padding: 18px 0 0 60px;
    color: var(--text-light);
    font-size: 19px;
    font-weight: 300;
  }
  .contact-list li { display: flex; line-height: 38px; }
  .contact-list .label { width: 70px; font-size: 13px; }
  .trainer-photo {
    position: absolute;
    right: 70px;
    top: 150px;
    width: 230px;
    height: 330px;
    background: linear-gradient(160deg, var(--photo-tone-a), var(--photo-tone-b));
    border-radius: 4px;
  }

  /* Back */
  .back-band {
    position: absolute;
    left: 0; right: 0;
    top: 262px;
    height: 140px;
    background: var(--ink);
  }
  .back-band__title {
    position: absolute;
    left: 60px;
    top: 44px;
    font-family: "Oswald", sans-serif;
    font-weight: 600;
    font-size: 40px;
    letter-spacing: 6px;
    color: var(--paper);
    text-transform: uppercase;
    white-space: nowrap;
  }
  .mascot-illustration {
    position: absolute;
    left: 300px;
    top: 60px;
    width: 240px;
    height: 202px;
    background: linear-gradient(180deg, #3a3a3a, var(--illustration-tone));
    border-radius: 6px 6px 0 0;
  }
</style>
</head>
<body>

<section class="card card--front">
  <div class="brand">
    <span class="brand__dot"></span>
    <span class="brand__name">Pine Ridge Canine Coaching</span>
  </div>
  <div class="contact-band">
    <div class="contact-band__name">Trevor Holloway</div>
    <ul class="contact-list">
      <li><span class="label">Tel</span><span>: 555-304-7162</span></li>
      <li><span class="label">Web</span><span>: www.pineridgecanine.example</span></li>
      <li><span class="label">Email</span><span>: info@pineridgecanine.example</span></li>
    </ul>
  </div>
  <div class="trainer-photo" role="img" aria-label="Photo of the trainer standing with two dogs sitting attentively at his feet"></div>
</section>

<section class="card card--back">
  <div class="back-band">
    <div class="back-band__title">Pine Ridge Canine Coaching</div>
  </div>
  <div class="mascot-illustration" role="img" aria-label="Black and white illustration of a Doberman wearing a chain collar with a paw tag"></div>
</section>

</body>
</html>
```